Meadowlark Learning Growth Partners (MLGP)

This is a professional business card. Logo and picture are a must on the front of the card. I am an educational consultant. I have been consulting for the past three years for a company. I am now opening my own company. My goal for my consulting company is to eventually consult all over America.

Target Market(s)

Educators, schools, professionals

Industry/Entity Type

Consulting

Contact Information for Business Card

Picture/logo on front, simple modern design

Font styles to use
Serif

Colors
85abd2
0355a3
3176b5
cedeed

Requirements
Must have
• picture, logo,
• Odessa Pruitt, Ed.S
• address 5073 Cormorant ridge Dr. Nashville, TN 37940
• Cell:616-555-0148
• Office: 629-555-0172
• www.Mlgpedu.example
• pruittodessa@mailbox.example

```html
<!DOCTYPE html>
<html lang="en">
<head>
<meta charset="utf-8">
<title>Meadowlark Learning Growth Partners — Business Card</title>
<link rel="stylesheet" href="https://fonts.googleapis.com/css2?family=Roboto+Serif:opsz,wght@8..144,300;8..144,400;8..144,700&display=swap">
<style>
  :root {
    --navy: #033877;
    --name-blue: #1b57a8;
    --photo-blue: #4a78bd;
    --photo-light: #85abd2;
    --photo-pale: #cedeed;
    --white: #ffffff;
    --ink-grey: #3a3a3a;
    --backdrop-top: #d9dadc;
    --backdrop-bottom: #c9cacc;
  }
  html, body {
    margin: 0;
    padding: 0;
    width: 960px;
    height: 1200px;
    overflow: hidden;
  }
  body {
    position: relative;
    background: linear-gradient(180deg, var(--backdrop-top), var(--backdrop-bottom));
    font-family: "Roboto Serif", Georgia, serif;
  }
  .card {
    position: absolute;
    left: 28px;
    width: 906px;
    height: 517px;
    background: var(--white);
    box-shadow: 0 10px 24px rgba(0, 0, 0, 0.22);
  }
  .card svg { display: block; width: 100%; height: 100%; }
  .card-front { top: 41px; }
  .card-back { top: 633px; }
  .brand-name { font-family: "Roboto Serif", Georgia, serif; font-weight: 700; letter-spacing: 3px; }
  .person-name { font-family: "Roboto Serif", Georgia, serif; font-weight: 700; fill: var(--name-blue); }
  .person-title { font-family: "Roboto Serif", Georgia, serif; font-weight: 300; fill: var(--ink-grey); }
  .contact-line { font-family: "Roboto Serif", Georgia, serif; font-weight: 300; fill: var(--white); }
  .icon { fill: none; stroke: var(--white); stroke-width: 2.4; stroke-linejoin: round; stroke-linecap: round; }
</style>
</head>
<body>

<section class="card card-front" aria-label="Business card front">
  <svg viewBox="0 0 1050 600" xmlns="http://www.w3.org/2000/svg">
    <defs>
      <radialGradient id="portrait-tone" cx="0.5" cy="0.42" r="0.6">
        <stop offset="0" stop-color="var(--photo-pale)"/>
        <stop offset="0.45" stop-color="var(--photo-light)"/>
        <stop offset="1" stop-color="var(--photo-blue)"/>
      </radialGradient>
    </defs>

    <polygon class="panel-main" points="0,0 712,0 0,596" fill="var(--navy)"/>
    <polygon class="panel-corner" points="14,600 289,370 508,600" fill="var(--navy)"/>

    <g class="brand-mark">
      <rect x="146" y="96" width="74" height="74" fill="var(--white)"/>
      <text class="brand-name" x="183" y="283" text-anchor="middle" font-size="58" fill="var(--white)">MLGP</text>
    </g>

    <circle class="portrait" cx="749" cy="268" r="167" fill="url(#portrait-tone)" role="img" aria-label="Portrait photo of Odessa Pruitt"/>

    <text class="person-name" x="749" y="486" text-anchor="middle" font-size="36">Odessa Pruitt</text>
    <text class="person-title" x="749" y="531" text-anchor="middle" font-size="36">Ed.S</text>
  </svg>
</section>

<section class="card card-back" aria-label="Business card back">
  <svg viewBox="0 0 1050 600" xmlns="http://www.w3.org/2000/svg">
    <polygon class="panel-top" points="205,0 424,232 696,0" fill="var(--navy)"/>
    <polygon class="panel-main" points="0,600 1051,600 1051,0 724,0" fill="var(--navy)"/>

    <g class="brand-mark">
      <rect x="126" y="150" width="74" height="74" fill="var(--navy)"/>
      <text class="brand-name" x="163" y="346" text-anchor="middle" font-size="58" fill="var(--navy)">MLGP</text>
    </g>

    <g class="contact-list" text-anchor="end" font-size="27">
      <text class="contact-line" x="888" y="287">616-555-0148</text>
      <text class="contact-line" x="888" y="348">629-555-0172</text>
      <text class="contact-line" x="888" y="405">www.Mlgpedu.example</text>
      <text class="contact-line" x="888" y="461">pruittodessa@mailbox.example</text>
      <text class="contact-line" x="888" y="517">5073 Cormorant ridge Dr. Nashville, TN 37940</text>
    </g>

    <g class="contact-icons">
      <g class="icon icon-mobile">
        <rect x="963" y="263" width="16" height="30" rx="3"/>
        <line x1="969" y1="288" x2="973" y2="288"/>
      </g>
      <g class="icon icon-phone">
        <path d="M955,336 q16,-10 32,0 l-2,6 h-6 l-1,-4 h-14 l-1,4 h-6 z"/>
        <rect x="959" y="344" width="24" height="11" rx="2"/>
      </g>
      <g class="icon icon-globe">
        <circle cx="971" cy="397" r="14"/>
        <ellipse cx="971" cy="397" rx="6" ry="14"/>
        <line x1="957" y1="397" x2="985" y2="397"/>
        <line x1="959" y1="390" x2="983" y2="390"/>
        <line x1="959" y1="404" x2="983" y2="404"/>
      </g>
      <g class="icon icon-mail">
        <rect x="955" y="442" width="32" height="22"/>
        <polyline points="955,442 971,455 987,442"/>
        <line x1="955" y1="464" x2="966" y2="453"/>
        <line x1="987" y1="464" x2="976" y2="453"/>
      </g>
      <g class="icon icon-pin">
        <path d="M971,527 c-10,-12 -15,-18 -15,-25 a15,15 0 0 1 30,0 c0,7 -5,13 -15,25 z"/>
        <circle cx="971" cy="502" r="5"/>
      </g>
    </g>
  </svg>
</section>

</body>
</html>
```